Boutique custom software development company needs new business card

Our nearly 20 year old custom software development company would like to better include the fact that we are now providing Bitcoin services. These new services are B2B include education (how to acquire and securely hold Bitcoin) and integrating Bitcoin payments into existing ecommerce sites or other existing systems. Please keep the card clean and simple. Attached is our current design and some other files. vexalon.example

Target Market(s)

businesses owners interested in long term relationship

Industry/Entity Type

Custom software development and Bitcoin

Contact Information for Business Card

Marcus Ellwood, marcus@vexalon.example, vexalon.example, (888) 555-VEXAL

Font styles to use
Other font styles liked:
• monospace

Requirements
Must have
• double-sided
Nice to have
• clean and simple
Should not have
• physical address

```html
<!DOCTYPE html>
<html lang="en">
<head>
<meta charset="utf-8">
<title>Vexalon business card</title>
<link rel="stylesheet" href="https://fonts.googleapis.com/css2?family=Montserrat:wght@400;600;800&family=Lato:wght@400&display=swap">
<style>
  :root {
    --backdrop: #2a2a2a;
    --card-light: #f4f4f4;
    --card-dark: #0b0b0b;
    --brand-blue: #3d75c4;
    --brand-orange: #f07d22;
    --white: #ffffff;
  }
  * { box-sizing: border-box; margin: 0; padding: 0; }
  html, body {
    width: 1200px;
    height: 900px;
    overflow: hidden;
    background: var(--backdrop);
  }
  .sheet {
    width: 1200px;
    height: 900px;
    display: flex;
    flex-direction: column;
    align-items: center;
    justify-content: center;
    gap: 50px;
  }
  .card {
    width: 600px;
    height: 343px;
    border-radius: 24px;
    position: relative;
    overflow: hidden;
  }
  .card-front {
    background: var(--card-light);
    display: flex;
    align-items: center;
  }
  .brand-block {
    width: 318px;
    flex: none;
    padding-left: 52px;
    padding-right: 24px;
    padding-top: 44px;
  }
  .brand-name {
    font-family: "Montserrat", sans-serif;
    font-weight: 800;
    font-size: 38px;
    letter-spacing: 0.5px;
    color: var(--brand-blue);
    text-transform: uppercase;
    line-height: 1;
    white-space: nowrap;
  }
  .brand-tagline {
    font-family: "Lato", sans-serif;
    font-size: 14px;
    color: var(--brand-blue);
    margin-top: 6px;
    white-space: nowrap;
  }
  .divider {
    width: 1px;
    height: 96px;
    flex: none;
    background: var(--brand-blue);
    margin-top: 10px;
  }
  .contact-block {
    padding-left: 26px;
    padding-bottom: 30px;
    font-family: "Montserrat", sans-serif;
  }
  .contact-name {
    font-weight: 600;
    font-size: 19px;
    letter-spacing: 1px;
    color: var(--brand-orange);
    text-transform: uppercase;
    margin-bottom: 8px;
    white-space: nowrap;
  }
  .contact-line {
    display: flex;
    align-items: center;
    gap: 8px;
    font-size: 13px;
    color: var(--brand-blue);
    line-height: 1.55;
    white-space: nowrap;
  }
  .contact-icon {
    width: 12px;
    height: 12px;
    flex: none;
  }
  .card-back {
    background: var(--card-dark);
    display: flex;
    align-items: center;
    justify-content: center;
  }
  .brand-name-reversed {
    font-family: "Montserrat", sans-serif;
    font-weight: 800;
    font-size: 68px;
    letter-spacing: 2px;
    color: var(--white);
    text-transform: uppercase;
  }
</style>
</head>
<body>
<main class="sheet">
  <section class="card card-front" aria-label="Card front">
    <div class="brand-block">
      <div class="brand-name">Vexalon</div>
      <div class="brand-tagline">custom software &amp; bitcoin services</div>
    </div>
    <div class="divider"></div>
    <div class="contact-block">
      <div class="contact-name">Marcus Ellwood</div>
      <div class="contact-line">
        <svg class="contact-icon" viewBox="0 0 24 24" aria-hidden="true"><path fill="var(--brand-orange)" d="M6.6 10.8a15 15 0 0 0 6.6 6.6l2.2-2.2a1 1 0 0 1 1-.25 11.4 11.4 0 0 0 3.6.57 1 1 0 0 1 1 1V20a1 1 0 0 1-1 1A17 17 0 0 1 3 4a1 1 0 0 1 1-1h3.5a1 1 0 0 1 1 1c0 1.25.2 2.45.57 3.57a1 1 0 0 1-.25 1z"/></svg>
        <span>(888) 555-VEXAL</span>
      </div>
      <div class="contact-line">
        <svg class="contact-icon" viewBox="0 0 24 24" aria-hidden="true"><path fill="var(--brand-orange)" d="M2 5h20v14H2z"/><path fill="none" stroke="var(--card-light)" stroke-width="2" d="M2 5l10 8 10-8"/></svg>
        <span>marcus@vexalon.example</span>
      </div>
      <div class="contact-line">
        <svg class="contact-icon" viewBox="0 0 24 24" aria-hidden="true"><circle cx="12" cy="12" r="10" fill="var(--brand-orange)"/><path fill="none" stroke="var(--card-light)" stroke-width="1.5" d="M2 12h20M12 2c3 3 3 17 0 20M12 2c-3 3-3 17 0 20"/></svg>
        <span>vexalon.example</span>
      </div>
    </div>
  </section>
  <section class="card card-back" aria-label="Card back">
    <div class="brand-name-reversed">Vexalon</div>
  </section>
</main>
</body>
</html>
```